Rug Cleaning Web Design Project

We need a web design for our cleaning company. We currently have a web page but are not happy with its design. We currently offer fine rug cleaning,upholstery cleaning, and residential and commercial carpet cleanning. We also offer water damage restoration. For our rug cleaning services we offer : Enzyme treatments for pet contamination and odor removal, application of stain protection that is designed for the fine textiles used in rug construction, application of treatments designed to prevent moth damage and pads designed to be used under rugs.Our current web site is harborlinewash.example. We are intrested in a design with similar information to the web page of Velmora Rug Cleaners INC. We would like to use the colors that are present in our logo that will be uploaded with this description. We would also like this new page to be linked to our other address fibertendpro.example. We would like the deign to be visually attractive but not "too busy".
Updates

Please include pictures of rugs, or people washing rugs if possible. We do not offer maid type cleaning services. We would not be interested in designs including pictures depicting that type service. Thanks for your hard work on this project.

Dale Hutchins

Industry/Entity Type

Residential

Requirements
Must have
• This page must be viewable on smart phones and tablets.

```html
<!DOCTYPE html>
<html lang="en">
<head>
<meta charset="utf-8">
<meta name="viewport" content="width=device-width, initial-scale=1">
<title>FiberTend Pro – Harborline Cleaning, LLC</title>
<link href="https://fonts.googleapis.com/css2?family=Arimo:wght@400;700&family=Ubuntu:wght@400;500&display=swap" rel="stylesheet">
<style>
:root{
  --cream:#ffffd9;
  --red-top:#ad0a33;
  --red-bottom:#6c0420;
  --ink:#1e1e1e;
  --body-text:#5a5a5a;
  --link-blue:#2d5a8e;
  --footer:#1f1f1c;
  --frame:#e8e6c8;
  --sale-white:#fffbe6;
  --sale-yellow:#ffd400;
  --sale-orange:#ff7a00;
}
*{box-sizing:border-box;margin:0;padding:0}
html,body{width:980px;height:1200px;overflow:hidden;background:var(--cream)}
body{font-family:"Arimo",Arial,sans-serif;color:var(--ink)}
.page{position:relative;width:980px;height:1200px}

/* header */
.brand{position:absolute;left:60px;top:26px;display:flex;align-items:center;gap:14px}
.brand-mark{width:44px;height:44px;border-radius:50%;background:#1e74c8}
.brand-name{font-size:40px;font-weight:700;letter-spacing:-1px;color:#222;line-height:1}
.brand-tagline{font-size:13px;letter-spacing:4px;color:#444;margin-top:4px}
.contact{position:absolute;right:40px;top:42px;text-align:right}
.contact-address{font-size:14px}
.contact-phone{font-size:28px;font-weight:700;margin-top:4px;display:flex;align-items:center;justify-content:flex-end;gap:8px}

/* nav */
.main-nav{position:absolute;left:20px;top:130px;width:940px;height:62px;background:linear-gradient(var(--red-top),var(--red-bottom));display:flex;padding-left:105px}
.main-nav a{display:flex;align-items:center;padding:0 20px;color:#fff;font-size:13px;font-weight:700;text-decoration:none;text-shadow:0 1px 1px rgba(0,0,0,.5);border-left:1px solid rgba(0,0,0,.3)}
.main-nav a:last-child{border-right:1px solid rgba(0,0,0,.3)}

/* hero */
.hero{position:absolute;left:20px;top:202px;width:940px;height:370px;box-shadow:0 18px 14px -10px rgba(0,0,0,.45)}
.hero-photo{position:absolute;inset:0;background:
  radial-gradient(circle at 22% 70%,#2f9a36 0 16%,transparent 30%),
  radial-gradient(circle at 15% 20%,#ff8a12 0 14%,transparent 28%),
  radial-gradient(circle at 60% 45%,#e8243c 0 25%,transparent 45%),
  radial-gradient(circle at 95% 15%,#c9d22a 0 10%,transparent 25%),
  linear-gradient(90deg,#b8452a,#d62a3a 60%,#a81b2c)}
.hero-offer{position:absolute;left:0;top:0;width:300px;height:100%;background:linear-gradient(160deg,#7c1a3c,#5a0c22 60%,#3a0a14)}
.offer-text{position:absolute;left:16px;top:30px;line-height:1}
.offer-sale{font-size:92px;color:var(--sale-white);letter-spacing:-2px}
.offer-sub{font-size:22px;color:var(--sale-yellow);margin-top:4px}
.offer-line{font-size:56px;color:var(--sale-yellow);margin-top:4px}
.offer-pct{font-size:90px;color:var(--sale-orange);margin-top:2px}
.offer-off{font-size:64px;color:var(--sale-yellow);font-weight:700}

/* columns */
.column{position:absolute;top:612px;width:300px;height:446px}
.column-1{left:20px}.column-2{left:340px}.column-3{left:660px}
.column-title{height:48px;background:linear-gradient(var(--red-top),var(--red-bottom));color:#fff;font-family:"Ubuntu",Arial,sans-serif;font-size:22px;padding:12px 0 0 22px;letter-spacing:.5px;text-shadow:0 1px 1px rgba(0,0,0,.4)}
.photo-frame{margin-top:26px;border:1px solid var(--frame);padding:9px;background:var(--cream)}
.photo{display:block;height:136px;background:radial-gradient(circle at 20% 50%,#4a4f57 0 8%,transparent 14%),linear-gradient(120deg,#e0620c,#f59a2c 50%,#d95a0a)}
.body-text{font-size:12.5px;line-height:18px;color:var(--body-text)}
.column-1 .body-text{margin-top:20px;padding:0 2px}
.lead{margin-top:24px;font-size:15.5px;line-height:22px;color:var(--link-blue)}
.column-2 .body-text{margin-top:14px}
.column-2 .body-text + .body-text{margin-top:14px}
.read-more{position:absolute;left:0;bottom:0;width:150px;height:34px;background:linear-gradient(var(--red-top),var(--red-bottom));color:#fff;font-size:19px;font-weight:700;padding:6px 0 0 23px;text-decoration:none;text-shadow:0 1px 1px rgba(0,0,0,.4)}

.feature-list{list-style:none;margin-top:18px}
.feature{display:flex;gap:16px;padding:2px 0 10px;border-bottom:1px solid var(--frame);margin-bottom:10px}
.feature:last-child{border-bottom:0}
.thumb-frame{flex:none;width:100px;height:96px;border:1px solid var(--frame);padding:8px 9px}
.thumb{display:block;width:100%;height:100%}
.thumb-red{background:radial-gradient(circle at 40% 40%,#ff3a3a,#c8100c)}
.thumb-green{background:linear-gradient(90deg,#c2c420,#d8d83a 60%,#e6e680)}
.thumb-blue{background:linear-gradient(135deg,#8a9ad6,#c07ac0 50%,#6a9ac8)}
.feature-title{font-size:16px;line-height:21px;color:var(--link-blue);margin-top:8px}
.feature .body-text{font-size:12.5px;margin-top:4px}

/* footer */
.site-footer{position:absolute;left:20px;top:1084px;width:940px;height:96px;background:var(--footer);color:#fff;text-align:center;font-size:12.5px;line-height:17px;padding-top:27px}
</style>
</head>
<body>
<div class="page">
  <header>
    <div class="brand">
      <span class="brand-mark"></span>
      <div>
        <div class="brand-name">FiberTend Pro</div>
        <div class="brand-tagline">HARBORLINE CLEANING, LLC</div>
      </div>
    </div>
    <div class="contact">
      <div class="contact-address">418 Calloway Lane, Brookhaven, AL&nbsp; 35000</div>
      <div class="contact-phone">
        <svg width="24" height="24" viewBox="0 0 24 24" aria-hidden="true"><path d="M6.6 10.8c1.4 2.8 3.8 5.1 6.6 6.6l2.2-2.2c.3-.3.7-.4 1-.2 1.1.4 2.3.6 3.6.6.6 0 1 .4 1 1V20c0 .6-.4 1-1 1C10.6 21 3 13.4 3 4c0-.6.4-1 1-1h3.5c.6 0 1 .4 1 1 0 1.3.2 2.5.6 3.6.1.3 0 .7-.2 1z" fill="#222"/></svg>
        (256) 555-0142
      </div>
    </div>
  </header>

  <nav class="main-nav">
    <a href="#">HOME</a>
    <a href="#">ABOUT US</a>
    <a href="#">RUG WASHING</a>
    <a href="#">WATER DAMAGE</a>
    <a href="#">CARPET CLEANING</a>
    <a href="#">CONTACT</a>
  </nav>

  <section class="hero">
    <div class="hero-photo" role="img" aria-label="Close-up photo of colourful rolled woven rugs in red, green, orange and yellow"></div>
    <div class="hero-offer">
      <div class="offer-text">
        <div class="offer-sale">SALE</div>
        <div class="offer-sub">SAPERET CONSEQUAT</div>
        <div class="offer-line">MEA ET</div>
        <div class="offer-pct">50%</div>
        <div class="offer-off">OFF</div>
      </div>
    </div>
  </section>

  <section class="column column-1">
    <h2 class="column-title">VIDE IMPERDIET</h2>
    <div class="photo-frame"><span class="photo" role="img" aria-label="Photo of a vacuum cleaner head on an orange shag rug"></span></div>
    <p class="body-text">Lorem ipsum dolor sit amet, eam nusquam similique sadipscing eu, ius mutat periculis disputationi ea, id cum sale persecuti. Vide imperdiet ea mei, sed dictas appetere oporteat ne. Ignota inimicus recteque est te, paulo graeci ornatus sit ea. Usu dicta senserit dissentiunt eu, graecis incorrupte usu id, ei laoreet principes nam.</p>
    <a class="read-more" href="#">Read more</a>
  </section>

  <section class="column column-2">
    <h2 class="column-title">VIDE IMPERDIET</h2>
    <p class="lead">Lorem ipsum dolor sit amet, eam nusquam similique sadipscing eu, ius mutat periculis disputationi ea, id cum</p>
    <p class="body-text">Lorem ipsum dolor sit amet, eam nusquam similique sadipscing eu, ius mutat periculis disputationi ea, id cum sale persecuti. Vide imperdiet ea mei, sed dictas appetere oporteat ne. Ignota inimicus recteque est te, paulo graeci</p>
    <p class="body-text">Lorem ipsum dolor sit amet, eam nusquam similique sadipscing eu, ius mutat periculis disputationi ea, id cum sale persecuti. Vide imperdiet ea mei, sed dictas appetere oporteat ne. Ignota inimicus recteque est te, paulo graeci ornatus sit ea. Usu dicta senserit dissentiunt eu, graecis incorrupte usu id, ei laoreet principes nam.</p>
    <a class="read-more" href="#">Read more</a>
  </section>

  <section class="column column-3">
    <h2 class="column-title">VIDE IMPERDIET</h2>
    <ul class="feature-list">
      <li class="feature">
        <div class="thumb-frame"><span class="thumb thumb-red" role="img" aria-label="Photo of red shag carpet fibres"></span></div>
        <div><h3 class="feature-title">VIDE IMPERDIET LABORIS</h3><p class="body-text">Lorem ipsum dolor sit amet, eam nusquam similique</p></div>
      </li>
      <li class="feature">
        <div class="thumb-frame"><span class="thumb thumb-green" role="img" aria-label="Photo of a vacuum cleaning a yellow-green carpet"></span></div>
        <div><h3 class="feature-title">VIDE IMPERDIET LABORIS</h3><p class="body-text">Lorem ipsum dolor sit amet, eam nusquam similique</p></div>
      </li>
      <li class="feature">
        <div class="thumb-frame"><span class="thumb thumb-blue" role="img" aria-label="Photo of a brush scrubbing a patterned rug"></span></div>
        <div><h3 class="feature-title">VIDE IMPERDIET LABORIS</h3><p class="body-text">Lorem ipsum dolor sit amet, eam nusquam similique</p></div>
      </li>
    </ul>
    <a class="read-more" href="#">Read more</a>
  </section>

  <footer class="site-footer">
    <p>Copyright © 2012 Harborline Cleaning, LLC</p>
    <p>Nec et erant clita consul, ius eu mazim nullam euripidis, his velit percipit et. Eam mundi</p>
    <p>Nec et erant clita consul, ius eu mazim nullam euripidis, his</p>
  </footer>
</div>
</body>
</html>
```